Qorvani Holdings Business Card

Create a two sided, high gloss, quality business card for Qorvani Holdings.

Target Market(s)

People wanting to purchase, scale, and sell businesses.

Industry/Entity Type

Entrepreneurs

Contact Information for Business Card

One line: Tessa Ruble, CPA, CMA Another line: Entrepreneur & Investor Another line: Business Ownership Transition Expert Another line: Multi-State Licensed Real Estate Broker Phone 954-QORVANI (767-8264) Email Tessa@Qorvani Holdings.com Website www.Qorvani.com

Requirements
Must have
• Black Card, logo on one side, all other information on the other side including a small logo.
Nice to have
• Possibly add a tagline "Helping entrepreneurs live a life they don't need a vacation from"
Should not have
• There will not be a mailing address on these cards.

```html
<!DOCTYPE html>
<html lang="en">
<head>
<meta charset="utf-8">
<title>Qorvani Holdings Business Card</title>
<link href="https://fonts.googleapis.com/css2?family=Montserrat:wght@500;600;700;800&family=Open+Sans:wght@400;600&display=swap" rel="stylesheet">
<style>
  :root {
    --backdrop: #3f3f3f;
    --card-black: #0c0c0c;
    --gold: #d9b54a;
    --gold-light: #f6e08c;
    --gold-deep: #a9801f;
    --text-light: #e9e9e9;
    --band-text: #111;
  }
  * { margin: 0; padding: 0; box-sizing: border-box; }
  html, body { width: 1200px; height: 801px; overflow: hidden; }
  body {
    background: radial-gradient(ellipse at 50% 40%, #4a4a4a 0%, var(--backdrop) 60%, #333 100%);
    position: relative;
    font-family: "Open Sans", sans-serif;
  }
  .card {
    position: absolute;
    top: 252px;
    width: 520px;
    height: 297px;
    background: var(--card-black);
    border: 1.5px solid var(--gold-deep);
    box-shadow: 0 14px 30px rgba(0,0,0,0.45);
    overflow: hidden;
  }
  .card--front { left: 60px; }
  .card--back { left: 620px; }

  /* Front side */
  .front-logo {
    position: absolute;
    left: 26px;
    top: 40px;
    display: flex;
    align-items: center;
    gap: 10px;
    font-family: "Montserrat", sans-serif;
    font-weight: 700;
    font-size: 24px;
    color: var(--gold);
    letter-spacing: 0.2px;
  }
  .logo-dot {
    width: 30px; height: 30px;
    border-radius: 50%;
    border: 2px solid var(--gold);
  }
  .name-band {
    position: absolute;
    left: 0;
    top: 108px;
    width: 520px;
    height: 30px;
    background: linear-gradient(90deg, var(--gold-deep) 0%, var(--gold-light) 30%, var(--gold) 60%, var(--gold-light) 85%, var(--gold-deep) 100%);
  }
  .name-band__text {
    position: absolute;
    left: 26px;
    top: 5px;
    font-family: "Montserrat", sans-serif;
    font-size: 16px;
    color: var(--band-text);
    white-space: nowrap;
  }
  .name-band__text strong { font-weight: 800; }
  .name-band__text span { font-weight: 500; }
  .portrait {
    position: absolute;
    right: 14px;
    top: 0;
    width: 210px;
    height: 297px;
    background: linear-gradient(180deg, #6b4a2c 0%, #7a5634 30%, #e3b84a 48%, #1e2536 62%, #141a28 100%);
    opacity: 0.95;
  }
  .titles {
    position: absolute;
    left: 26px;
    top: 150px;
    color: var(--text-light);
    font-size: 12.5px;
    line-height: 17px;
  }
  .contacts {
    position: absolute;
    left: 26px;
    top: 212px;
    list-style: none;
    color: var(--text-light);
    font-size: 12.5px;
    line-height: 19px;
  }
  .contacts li { display: flex; align-items: center; gap: 8px; }
  .contacts svg { width: 11px; height: 11px; flex: none; }

  /* Back side */
  .back-logo {
    position: absolute;
    left: 0; right: 0; top: 0; bottom: 0;
    display: flex;
    align-items: center;
    justify-content: center;
    gap: 16px;
    font-family: "Montserrat", sans-serif;
    font-weight: 700;
    font-size: 38px;
    color: var(--gold);
  }
  .back-logo .logo-dot { width: 54px; height: 54px; border-width: 3px; }
</style>
</head>
<body>

<section class="card card--front" aria-label="Card front">
  <div class="portrait" role="img" aria-label="Portrait photo of Tessa Ruble in a dark blazer and yellow blouse"></div>
  <div class="front-logo"><span class="logo-dot"></span>Qorvani Holdings</div>
  <div class="name-band">
    <p class="name-band__text"><strong>TESSA RUBLE,</strong> <span>CPA, CMA</span></p>
  </div>
  <div class="titles">
    <p>Entrepreneur &amp; Investor</p>
    <p>Business Ownership Transition Expert</p>
    <p>Multi-State Licensed Real Estate Broker</p>
  </div>
  <ul class="contacts">
    <li>
      <svg viewBox="0 0 12 12"><path d="M3 1 L5 3.5 L4 5 Q5 7 7 8 L8.5 7 L11 9 L9.5 11 Q5 11 1 3 Z" fill="#d9b54a"/></svg>
      954-QORVANI (767-8264)
    </li>
    <li>
      <svg viewBox="0 0 12 12"><rect x="1" y="2.5" width="10" height="7" fill="#d9b54a"/><path d="M1 2.5 L6 6.5 L11 2.5" stroke="#0c0c0c" fill="none"/></svg>
      Tessa@Qorvani Holdings.com
    </li>
    <li>
      <svg viewBox="0 0 12 12"><circle cx="6" cy="6" r="5" fill="none" stroke="#d9b54a" stroke-width="1.4"/><path d="M1 6 H11 M6 1 Q3 6 6 11 Q9 6 6 1" stroke="#d9b54a" fill="none"/></svg>
      www.Qorvani.com
    </li>
  </ul>
</section>

<section class="card card--back" aria-label="Card back">
  <div class="back-logo"><span class="logo-dot"></span>Qorvani Holdings</div>
</section>

</body>
</html>
```